Label for natural soft drink / juice

Please see the briefing attached as PDF

Required is a label design that adds a frame for a range of different labels linked to a variety of tastes for a natural, organic, sparkling beverage in a multi-use, environmentally friendly returnable clear glass bottle.
The 2 first tastes are rhubarb and apple
The label will be a paper label sticked at the front side of the bottle.
No glossy or shiny appearance as it does not fit the organic image
No color restrictions in general, but
Blue better than green
Matt better than glossy
Fit of colours on one label essential, so no “crying colour mixture” (great also: complementary contrasts like blue/orange)
Handpainted better than photorealistic
Simple better than overcrowded
Smart, funny intelligent a lot better than same standard as everywhere
For the image consider subtile reminiscence to the fruit or other stuff linked to the fruit (even “across 3 corners”, so a bit far away) as a nice additional asset

Target Market(s)

modern restaurants with high quality food, often with organic and regional products on the menu.

Font styles to use
Serif
Sans Serif
Script

Requirements
Nice to have
• the fruit of the current taste or something linked to the fruit as e.g. reminiscence to well known story or history of the fruit
Should not have
• too many elements on the label. simplicity is key

```html
<!DOCTYPE html>
<html lang="en">
<head>
<meta charset="utf-8">
<title>Hartwells Organic Drinks – Labels</title>
<link href="https://fonts.googleapis.com/css2?family=Roboto:wght@300;400;700&family=Roboto+Condensed:wght@700&display=swap" rel="stylesheet">
<style>
  :root {
    --page-bg: #ffffff;
    --apple-paper: #f4e7d1;
    --rhubarb-paper: #f6cdb8;
    --brand-green: #4c9b5e;
    --rule-brown: #c4834a;
    --apple-type: #c07a3c;
    --rhubarb-type: #a8563f;
    --apple-tone-a: #e06a4c;
    --apple-tone-b: #d8412f;
    --rhubarb-tone-a: #c96a66;
    --rhubarb-tone-b: #9aa66a;
  }
  * { margin: 0; padding: 0; box-sizing: border-box; }
  html, body {
    width: 1200px;
    height: 1200px;
    overflow: hidden;
    background: var(--page-bg);
  }
  .label-range {
    width: 1200px;
    height: 1200px;
    display: flex;
    justify-content: center;
    align-items: center;
    gap: 120px;
  }
  .label {
    width: 440px;
    height: 640px;
    display: block;
  }
  .label .arch-name {
    font-family: "Roboto", Arial, sans-serif;
    font-weight: 700;
    font-size: 44px;
    letter-spacing: 7px;
    fill: var(--brand-green);
  }
  .label .organic {
    font-family: "Roboto", Arial, sans-serif;
    font-weight: 400;
    font-size: 15px;
    letter-spacing: 1px;
    fill: var(--brand-green);
  }
  .label .flavour {
    font-family: "Roboto", Arial, sans-serif;
    font-weight: 300;
    font-size: 28px;
    letter-spacing: 4px;
  }
  .label--apple .flavour { fill: var(--apple-type); }
  .label--rhubarb .flavour { fill: var(--rhubarb-type); }
  .label .rule { stroke: var(--rule-brown); stroke-width: 1.6; }
  .label .thin-rule { stroke: var(--brand-green); stroke-width: 1; }
  .label .maker-name {
    font-family: "Roboto Condensed", "Arial Narrow", sans-serif;
    font-weight: 700;
    font-size: 44px;
    letter-spacing: 2px;
    fill: var(--brand-green);
  }
  .label .maker-dot { fill: none; stroke: var(--brand-green); stroke-width: 2; }
  .label .tagline {
    font-family: "Roboto", Arial, sans-serif;
    font-weight: 300;
    font-size: 13px;
    letter-spacing: 1px;
    fill: var(--brand-green);
  }
</style>
</head>
<body>
<main class="label-range">

  <svg class="label label--apple" viewBox="0 0 440 640" aria-label="Hartwells organic apple drink label">
    <defs>
      <path id="arch-text-apple" d="M55,190 A190,150 0 0 1 385,190"/>
      <linearGradient id="apple-area-tone" x1="0" y1="0" x2="1" y2="1">
        <stop offset="0%" stop-color="var(--apple-tone-a)"/>
        <stop offset="100%" stop-color="var(--apple-tone-b)"/>
      </linearGradient>
    </defs>
    <path class="label-paper" d="M0,160 A240,170 0 0 1 440,160 L440,640 L0,640 Z" fill="var(--apple-paper)"/>
    <text class="arch-name"><textPath href="#arch-text-apple" startOffset="50%" text-anchor="middle">HARTWELLS</textPath></text>

    <rect class="fruit-image" x="150" y="205" width="140" height="110" rx="10"
          fill="url(#apple-area-tone)" role="img" aria-label="Photo of a red apple with a green leaf"/>

    <line class="rule" x1="70" y1="340" x2="370" y2="340"/>
    <text class="organic" x="220" y="362" text-anchor="middle">ORGANIC</text>
    <text class="flavour" x="220" y="394" text-anchor="middle">APPLE DRINK</text>
    <line class="rule" x1="70" y1="408" x2="370" y2="408"/>

    <circle class="maker-dot" cx="220" cy="492" r="16"/>
    <text class="maker-name" x="220" y="565" text-anchor="middle">HARTWELLS</text>
    <line class="thin-rule" x1="110" y1="589" x2="160" y2="589"/>
    <text class="tagline" x="220" y="593" text-anchor="middle">Brewhouse</text>
    <line class="thin-rule" x1="280" y1="589" x2="330" y2="589"/>
  </svg>

  <svg class="label label--rhubarb" viewBox="0 0 440 640" aria-label="Hartwells organic rhubarb drink label">
    <defs>
      <path id="arch-text-rhubarb" d="M55,190 A190,150 0 0 1 385,190"/>
      <linearGradient id="rhubarb-area-tone" x1="0" y1="1" x2="1" y2="0">
        <stop offset="0%" stop-color="var(--rhubarb-tone-a)"/>
        <stop offset="100%" stop-color="var(--rhubarb-tone-b)"/>
      </linearGradient>
    </defs>
    <path class="label-paper" d="M0,160 A240,170 0 0 1 440,160 L440,640 L0,640 Z" fill="var(--rhubarb-paper)"/>
    <text class="arch-name"><textPath href="#arch-text-rhubarb" startOffset="50%" text-anchor="middle">HARTWELLS</textPath></text>

    <rect class="fruit-image" x="120" y="215" width="200" height="100" rx="10"
          fill="url(#rhubarb-area-tone)" role="img" aria-label="Photo of rhubarb stalks with leaves"/>

    <line class="rule" x1="70" y1="340" x2="370" y2="340"/>
    <text class="organic" x="220" y="362" text-anchor="middle">ORGANIC</text>
    <text class="flavour" x="220" y="394" text-anchor="middle">RHUBARB DRINK</text>
    <line class="rule" x1="70" y1="408" x2="370" y2="408"/>

    <circle class="maker-dot" cx="220" cy="492" r="16"/>
    <text class="maker-name" x="220" y="565" text-anchor="middle">HARTWELLS</text>
    <line class="thin-rule" x1="110" y1="589" x2="160" y2="589"/>
    <text class="tagline" x="220" y="593" text-anchor="middle">Brewhouse</text>
    <line class="thin-rule" x1="280" y1="589" x2="330" y2="589"/>
  </svg>

</main>
</body>
</html>
```